Elegant Business Cards & Letterhead

We will need the following that need to be designed: Letterhead and Business Cards, there winer will be re-hired for the balance of our stationary needs. Text for the cards and letterheads:

- Corporate Card instead of name
- landline: +971 (4) 632 7140
- mobile: +971 56 3918 065
- 800CARER
- email: dubai@velvet-oaks.example
- www.velvet-oaks.example
- PO Box 387261
Address: Castellan Tower Suite 1706, Dubai UAE

Thank you

Target Market(s)

VIPs, HNWI, High-end Families.

Industry/Entity Type

Luxury Market

Font styles to use
Other font styles liked:
• as explained

Colors

Designer to choose only greyscale colors for use in the design.

Requirements
Must have
• Elegant, Simple, Luxurious, Minimalistic
Nice to have
• Luxury, Golds, Engravings,
Should not have
• Much colors, funky,

```html
<!DOCTYPE html>
<html lang="en">
<head>
<meta charset="utf-8">
<title>Velvet Oaks — Stationery</title>
<link rel="stylesheet" href="https://fonts.googleapis.com/css2?family=Marcellus&family=Montserrat:wght@400;500&display=swap">
<style>
  :root {
    --backdrop: #e4e4e4;
    --paper: #f6f6f6;
    --card-light: #ececec;
    --card-dark: #262626;
    --gold: #a9824f;
    --ink: #2b2b2b;
  }
  * { margin: 0; padding: 0; box-sizing: border-box; }
  html, body { width: 1200px; height: 933px; overflow: hidden; }
  body {
    position: relative;
    background: var(--backdrop);
    font-family: "Montserrat", sans-serif;
    color: var(--ink);
  }
  .wordmark {
    font-family: "Marcellus", serif;
    color: var(--gold);
    letter-spacing: 0.04em;
    text-transform: uppercase;
    white-space: nowrap;
    text-align: center;
  }
  .contact {
    text-transform: uppercase;
    letter-spacing: 0.12em;
    text-align: center;
    white-space: nowrap;
  }
  .contact .label { font-size: 0.85em; }

  .letterhead {
    position: absolute;
    left: 101px; top: 55px;
    width: 546px; height: 774px;
    background: var(--paper);
  }
  .letterhead .wordmark {
    position: absolute; top: 30px; left: 0; right: 0;
    font-size: 23px;
  }
  .letterhead-footer {
    position: absolute; left: 0; right: 0; top: 713px;
  }
  .letterhead-footer .contact {
    font-size: 7.6px;
    line-height: 10.6px;
  }
  .letterhead-footer .tagline {
    margin-top: 4px;
    font-size: 6.2px;
    text-align: center;
    letter-spacing: 0.01em;
    white-space: nowrap;
  }

  .card {
    position: absolute;
    width: 300px; height: 174px;
  }
  .card-front {
    left: 769px; top: 381px;
    background: var(--card-dark);
  }
  .card-front .wordmark {
    position: absolute; left: 0; right: 0; top: 70px;
    font-size: 28px;
  }
  .card-back {
    left: 772px; top: 618px;
    background: var(--card-light);
  }
  .card-back .wordmark {
    position: absolute; left: 0; right: 0; top: 15px;
    font-size: 20px;
  }
  .card-back .contact {
    position: absolute; left: 0; right: 0; top: 85px;
    font-size: 8.4px;
    line-height: 14.5px;
    letter-spacing: 0.06em;
  }
</style>
</head>
<body>
  <section class="letterhead" aria-label="Letterhead">
    <div class="wordmark">Velvet Oaks</div>
    <footer class="letterhead-footer">
      <p class="contact"><span class="label">P</span> +971 (4) 632 7140 | <span class="label">M</span> +971 56 3918 065 | 800CARER | dubai@velvet-oaks.example</p>
      <p class="contact">Castellan Tower Suite 1706, Dubai UAE | PO Box 387261</p>
      <p class="contact">www.velvet-oaks.example</p>
      <p class="tagline">Private Household and Estate Services since 2016, based in Dubai with offices in London and Geneva</p>
    </footer>
  </section>

  <section class="card card-front" aria-label="Business card front">
    <div class="wordmark">Velvet Oaks</div>
  </section>

  <section class="card card-back" aria-label="Business card back">
    <div class="wordmark">Velvet Oaks</div>
    <div class="contact">
      <p><span class="label">P</span> +971 (4) 632 7140 | <span class="label">M</span> +971 56 3918 065</p>
      <p>dubai@velvet-oaks.example</p>
      <p>Castellan Tower Suite 1706, Dubai UAE</p>
      <p>PO Box 387261</p>
      <p>www.velvet-oaks.example</p>
    </div>
  </section>
</body>
</html>
```